Website Landing Page for Brightfall Systems

Create a custom designed website landing page for our business. Looking for a professional upscale design that incorporates our logo and logo colors into the theme. I want a standard fixed frame website, not a constant scrolling format that seems to be the trend. To start with I'm looking for more of the graphic design part, maybe a concept or theme, I don't expect to see a finished project. Not interested in generic templates or layouts.

The name of our company is Brightfall Systems and I've attached our logo below. I'd like to have the web page have the same look and feel of our logo, as well as the colors. Our company, Brightfall Systems does system design, installation, and programming, of residential and commercial Audio/Video and Automation systems. We do home theaters, lighting and building automation, video conferencing systems, security camera installations, conference rooms, projectors, distributed audio systems, and similar Technology projects. This will be a professional services/informational website. We will not sell products on this website. This website will be used to advertise our company and communicate our services to prospective customers. Having a well designed, professional and clean website is one way we want to distinguish our company from the competition.

Here are some examples of what I consider a professional well designed website
http://www.qorlamstudio.com/Work/

Last year we had our tradlo store designed (with PixelMarket) and I'm really happy with the way it turned out. You can see it at www.HolvenGearDepot.com I consider this to be a great design and looking for the same level of quality with this new website. However, do not copy or use any part of this design in this new project. This tradlo store is completely separate from our other company Brightfall Systems. I only mention this tradlo store an an example of good work.

Reason: Still going through designs.

Reason: Still working on project and have not had time to review all designs and request revisions.

Reason: Sill going through designs and requesting revisions

Reason: still going through all the submissions we received.

Target Market(s)

People interested in Audio/Video, home theaters, home automation. We do sales, system design, and programming. We typically work on larger projects with both residential and commercial customers.

Industry/Entity Type

Business

Number of Pages Required

1 page

Requirements
Must have
• Great design elements. Please use a white background. I think white goes well with our logo colors.

```html
<!DOCTYPE html>
<html lang="en">
<head>
<meta charset="utf-8">
<title>Brightfall Systems</title>
<link href="https://fonts.googleapis.com/css2?family=Montserrat:wght@500;600;700&family=Questrial&display=swap" rel="stylesheet">
<style>
:root{
  --white:#ffffff;
  --ink:#2b2b2b;
  --navy:rgba(30,42,70,.82);
  --teal:#2aa6c9;
  --green:#8cc760;
  --tile-teal-a:#b9e6e6;
  --tile-teal-b:#8fd3d6;
  --tile-green-a:#cdeebb;
  --tile-green-b:#a8dc8f;
  --label:#3a4a55;
  --quote:#8cc760;
  --arrow:#e7e27a;
  --grey:#b8b8b8;
  --footer:#555;
}
*{box-sizing:border-box;margin:0;padding:0}
html,body{width:1200px;height:818px;overflow:hidden;background:var(--white)}
body{position:relative;font-family:"Montserrat",sans-serif;color:var(--ink)}

.top-bar{position:absolute;left:0;top:0;width:1200px;height:52px}
.menu-icon{position:absolute;left:24px;top:22px;width:26px}
.menu-icon span{display:block;height:2px;background:var(--ink);margin-bottom:4px}
.brand-name{position:absolute;left:70px;top:22px;font-family:"Questrial",sans-serif;font-size:12px;letter-spacing:.3px}
.contact-email{position:absolute;right:22px;top:22px;font-family:"Questrial",sans-serif;font-size:11.5px}

.service-row{position:absolute;left:2px;top:52px;width:1196px;height:192px;display:grid;grid-template-columns:repeat(7,1fr);gap:3px}
.service-tile{position:relative;text-align:center;color:var(--label)}
.service-tile.teal{background:linear-gradient(160deg,var(--tile-teal-a),var(--tile-teal-b))}
.service-tile.green{background:linear-gradient(160deg,var(--tile-green-a),var(--tile-green-b))}
.service-tile svg{position:absolute;left:50%;top:54px;transform:translateX(-50%);width:66px;height:66px}
.tile-title{position:absolute;left:0;right:0;top:142px;font-weight:700;font-size:16.5px;letter-spacing:.4px}
.tile-sub{position:absolute;left:0;right:0;top:162px;font-weight:600;font-size:12px;letter-spacing:.6px}
.logo-tile{background:var(--white);display:flex;align-items:center;justify-content:center}
.logo-word{font-weight:700;font-size:23px;line-height:1.2;color:var(--teal);letter-spacing:.8px;text-align:center}

.hero{position:absolute;top:247px;height:358px}
.hero-left{left:0;width:598px;background:linear-gradient(180deg,#3f6fb0 0%,#6f9fd4 45%,#9fc3e6 100%)}
.hero-right{left:601px;width:599px;background:linear-gradient(160deg,#b9b6ae 0%,#8d8a84 45%,#454c5a 100%)}
.info-panel{position:absolute;background:var(--navy);color:var(--white)}
.welcome-panel{left:42px;top:286px;width:338px;height:209px;padding:14px 28px 0 22px}
.services-panel{left:836px;top:286px;width:334px;height:234px;padding:12px 17px 0 27px;text-align:right}
.panel-heading{font-family:"Questrial",sans-serif;font-size:21.5px;line-height:28px}
.panel-rule{width:96px;height:2px;background:var(--teal);margin:8px 0 14px}
.services-panel .panel-rule{margin:8px 0 8px auto}
.panel-copy{font-weight:600;font-size:9.2px;line-height:15px}
.panel-copy + .panel-copy{margin-top:15px}

.quote-card{position:absolute;left:460px;top:475px;width:298px;height:130px;background:var(--white);text-align:center}
.quote-text{position:absolute;left:0;right:0;top:34px;font-family:"Questrial",sans-serif;font-size:21px;line-height:28px;color:var(--quote)}
.quote-mark{position:absolute;font-family:Georgia,serif;font-size:44px;color:#d5cfb8;line-height:1}
.quote-open{left:14px;top:26px}
.quote-close{right:14px;top:66px}
.slide-dots{position:absolute;left:124px;top:110px;display:flex;gap:4px}
.slide-dots span{width:6px;height:6px;border-radius:50%;background:#c9c9c9}
.slide-dots span.active{background:var(--teal)}
.slide-arrow{position:absolute;top:527px;width:30px;height:60px}
.arrow-prev{left:20px}
.arrow-next{left:1142px}

.skyline{position:absolute;left:0;top:580px;width:1200px;height:170px;background:linear-gradient(180deg,rgba(255,255,255,0) 0%,rgba(200,210,220,.55) 35%,rgba(215,225,210,.5) 70%,var(--white) 100%)}

.footer-links{position:absolute;left:37px;top:767px;font-size:8.5px;font-weight:500;color:var(--footer);line-height:15px}
.footer-links a{color:var(--footer);text-decoration:none}
.client-row{position:absolute;left:430px;top:772px;width:750px;display:flex;justify-content:space-between;align-items:center}
.client-name{font-family:"Questrial",sans-serif;font-size:13px;color:var(--grey)}
</style>
</head>
<body>

<header class="top-bar">
  <div class="menu-icon"><span></span><span></span><span></span></div>
  <div class="brand-name">BRIGHTFALL SYSTEMS</div>
  <div class="contact-email">info@brightfallsystems.com</div>
</header>

<nav class="service-row">
  <div class="service-tile teal" role="img" aria-label="Automation systems tile over a tinted office photo">
    <svg viewBox="0 0 66 66" fill="none" stroke="#fff" stroke-width="4"><circle cx="33" cy="33" r="14"/><circle cx="33" cy="33" r="5"/><path d="M33 8v8M33 50v8M8 33h8M50 33h8M15 15l6 6M45 45l6 6M15 51l6-6M45 21l6-6"/></svg>
    <div class="tile-title">AUTOMATION</div><div class="tile-sub">SYSTEMS</div>
  </div>
  <div class="service-tile green" role="img" aria-label="System design tile over a tinted office photo">
    <svg viewBox="0 0 66 66" fill="none" stroke="#fff" stroke-width="4"><rect x="6" y="8" width="18" height="12"/><rect x="42" y="24" width="18" height="12"/><rect x="6" y="44" width="18" height="12"/><path d="M24 14h26v10M42 30H15v14"/></svg>
    <div class="tile-title">SYSTEM</div><div class="tile-sub">DESIGN</div>
  </div>
  <div class="service-tile teal" role="img" aria-label="Installation systems tile over a tinted room photo">
    <svg viewBox="0 0 66 66" fill="none" stroke="#fff" stroke-width="4"><circle cx="33" cy="33" r="28"/><circle cx="33" cy="33" r="18"/><circle cx="33" cy="33" r="8"/><path d="M33 33L52 14"/></svg>
    <div class="tile-title">INSTALLATION</div><div class="tile-sub">SYSTEMS</div>
  </div>
  <div class="service-tile logo-tile">
    <div class="logo-word">BRIGHTFALL<br>SYSTEMS</div>
  </div>
  <div class="service-tile green" role="img" aria-label="Audio and video solutions tile over a tinted room photo">
    <svg viewBox="0 0 66 66" fill="none" stroke="#fff" stroke-width="4"><rect x="6" y="18" width="34" height="38"/><path d="M46 44V12l14-4v30"/><circle cx="42" cy="46" r="5"/><circle cx="56" cy="40" r="5"/></svg>
    <div class="tile-title">AUDIO/VIDEO</div><div class="tile-sub">SOLUTIONS</div>
  </div>
  <div class="service-tile teal" role="img" aria-label="Automation systems tile over a tinted room photo">
    <svg viewBox="0 0 66 66" fill="none" stroke="#fff" stroke-width="4"><rect x="6" y="6" width="54" height="54" rx="4"/><path d="M20 46l26-26M36 20h10v10M20 36v10h10"/></svg>
    <div class="tile-title">AUTOMATION</div><div class="tile-sub">SYSTEMS</div>
  </div>
  <div class="service-tile green" role="img" aria-label="Programming solutions tile over a tinted room photo">
    <svg viewBox="0 0 66 66" fill="none" stroke="#fff" stroke-width="4"><rect x="4" y="8" width="58" height="38" rx="3"/><path d="M33 46v10M20 58h26M22 27l8 8 15-15"/></svg>
    <div class="tile-title">PROGRAMMING</div><div class="tile-sub">SOLUTIONS</div>
  </div>
</nav>

<div class="hero hero-left" role="img" aria-label="Glass office tower against a blue sky"></div>
<div class="hero hero-right" role="img" aria-label="Auditorium with projection screen and tiered seating"></div>

<section class="info-panel welcome-panel">
  <h1 class="panel-heading">Welcome to<br>Brightfall Systems</h1>
  <div class="panel-rule"></div>
  <p class="panel-copy">Lorem ipsum dolor sit amet, consectetur adipiscing elit, sed do eiusmod tempor incididunt ut labore et dolore magna aliqua. Ut enim ad minim veniam, quis nostrud exercitation ullamco laboris nisi ut aliquip ex ea commodo consequat. Duis aute irure dolor in reprehenderit in voluptate velit esse cillum dolore eu fugiat nulla pariatur.</p>
</section>

<section class="info-panel services-panel">
  <h2 class="panel-heading">Our Services</h2>
  <div class="panel-rule"></div>
  <p class="panel-copy">Lorem ipsum dolor sit amet, consectetur adipiscing elit, sed do eiusmod tempor incididunt ut labore et dolore magna aliqua. Ut enim ad minim veniam, quis nostrud exercitation ullamco laboris nisi ut aliquip ex ea commodo consequat. Duis aute irure dolor in reprehenderit in voluptate velit esse cillum dolore eu fugiat nulla pariatur.Lorem ipsum dolor sit amet, consectetur adipiscing elit,</p>
  <p class="panel-copy">sed do eiusmod tempor incididunt ut labore et dolore magna aliqua. Ut enim ad minim veniam, quis nostrud exercitation ullamco laboris nisi ut aliquip ex ea commo</p>
</section>

<div class="skyline" role="img" aria-label="Faded city skyline fading into white"></div>

<aside class="quote-card">
  <span class="quote-mark quote-open">&ldquo;</span>
  <p class="quote-text">The true definition<br>of luxury technology</p>
  <span class="quote-mark quote-close">&rdquo;</span>
  <div class="slide-dots"><span></span><span></span><span></span><span class="active"></span></div>
</aside>

<svg class="slide-arrow arrow-prev" viewBox="0 0 30 60" fill="none" stroke="var(--arrow)" stroke-width="2"><path d="M28 2L3 30l25 28"/></svg>
<svg class="slide-arrow arrow-next" viewBox="0 0 30 60" fill="none" stroke="var(--arrow)" stroke-width="2"><path d="M2 2l25 28L2 58"/></svg>

<footer>
  <div class="footer-links"><a href="#">Home</a> | <a href="#">About Us</a> | <a href="#">Contact Us</a><br>Copyright 2017 all rights reserved.</div>
  <div class="client-row">
    <span class="client-name">Northvale</span>
    <span class="client-name">Kestrel Mutual</span>
    <span class="client-name">Hartwell's</span>
    <span class="client-name">Orvane</span>
    <span class="client-name">Lumo Mart</span>
    <span class="client-name">Corrin Aldous</span>
    <span class="client-name">Pellow</span>
    <span class="client-name">Northvale</span>
    <span class="client-name">Hartwell's</span>
  </div>
</footer>

</body>
</html>
```